"Sail Past Amber Dunes" Book Cover Design

I am seeking a dynamic, modern, and professional cover design for a book focused on groundbreaking science that explores how a supplement called plasmalogens can revitalize the brain, prevent Alzheimer’s, and safeguard memories. The design should strike a balance between being visually appealing and conveying the seriousness of the topic.

Target Market(s)

The target audience includes individuals who are curious about cutting-edge science and proactive approaches to brain health, as well as those seeking to better understand how to protect their cognitive functions and memories. The cover should resonate with readers interested in health, science, and self-improvement, while reflecting the book’s informative and empowering tone.

Requirements
Must have
• The quotation across the top of the page (this is a placeholder for now, it will be changed eventually) and the author's name.
Should not have
• You don't need to use the puzzle idea!

```html
<!DOCTYPE html>
<html lang="en">
<head>
<meta charset="utf-8">
<title>Sail Past Amber Dunes — Book Cover</title>
<link href="https://fonts.googleapis.com/css2?family=Montserrat:ital,wght@0,500;0,700;0,800;1,700&display=swap" rel="stylesheet">
<style>
  :root {
    --paper: #f0f0f0;
    --paper-edge: #e6e6e6;
    --panel: #f8f8f8;
    --ink-dark: #939595;
    --ink-light: #b8b9ba;
    --ink-quote: #9a9b9c;
  }
  html, body {
    margin: 0;
    padding: 0;
    overflow: hidden;
  }
  .cover {
    position: relative;
    width: 927px;
    height: 1200px;
    overflow: hidden;
    background: radial-gradient(ellipse at center, var(--paper) 0%, var(--paper) 60%, var(--paper-edge) 100%);
    font-family: "Montserrat", sans-serif;
  }
  .panel {
    position: absolute;
    background: var(--panel);
  }
  .panel--quote { left: 164px; top: 107px; width: 299px; height: 162px; }
  .panel--title { left: 464px; top: 289px; width: 278px; height: 601px; }
  .panel--author { left: 480px; top: 900px; width: 278px; height: 127px; }

  .bracket {
    position: absolute;
    background: var(--ink-dark);
  }
  .bracket--quote-h { left: 378px; top: 107px; width: 85px; height: 11px; }
  .bracket--quote-v { left: 452px; top: 107px; width: 11px; height: 85px; }
  .bracket--author-v { left: 464px; top: 978px; width: 11px; height: 84px; }
  .bracket--author-h { left: 464px; top: 1049px; width: 84px; height: 13px; }

  .quote {
    position: absolute;
    right: 493px;
    top: 140px;
    margin: 0;
    text-align: right;
    color: var(--ink-quote);
    font-size: 16.5px;
    font-weight: 500;
    line-height: 22px;
  }
  .quote__source {
    display: block;
    font-weight: 700;
    font-style: italic;
  }

  .illustration {
    position: absolute;
    left: 176px;
    top: 306px;
    width: 283px;
    height: 584px;
    background: var(--ink-dark);
    border-radius: 140px 14px 14px 140px / 200px 14px 14px 200px;
  }

  .title {
    position: absolute;
    left: 464px;
    top: 289px;
    width: 278px;
    height: 601px;
    margin: 0;
  }
  .title svg { display: block; }
  .title text {
    font-family: "Montserrat", sans-serif;
    font-weight: 800;
  }
  .title .t-dark { fill: var(--ink-dark); }
  .title .t-light { fill: var(--ink-light); }

  .author {
    position: absolute;
    left: 502px;
    top: 981px;
    margin: 0;
    color: var(--ink-dark);
    font-size: 20px;
    font-weight: 700;
    line-height: 33px;
    letter-spacing: 0.5px;
  }
</style>
</head>
<body>
<main class="cover">
  <div class="panel panel--quote"></div>
  <div class="bracket bracket--quote-h"></div>
  <div class="bracket bracket--quote-v"></div>
  <blockquote class="quote">
    “An Incredible guide to protecting<br>your mind and memories.”
    <span class="quote__source">- Dr Omar Linde, MD</span>
  </blockquote>

  <div class="illustration" role="img" aria-label="Illustration of a grey brain hemisphere with white folds"></div>

  <div class="panel panel--title"></div>
  <h1 class="title" aria-label="Sail Past Amber Dunes">
    <svg width="278" height="601" viewBox="0 0 278 601" aria-hidden="true">
      <text class="t-dark" x="7" y="198" font-size="188" textLength="268" lengthAdjust="spacingAndGlyphs" transform="scale(1,0.75)">SAIL</text>
      <text class="t-light" x="7" y="282" font-size="98" textLength="268" lengthAdjust="spacingAndGlyphs">PAST</text>
      <text class="t-dark" x="7" y="392" font-size="136" textLength="268" lengthAdjust="spacingAndGlyphs">AM</text>
      <text class="t-dark" x="7" y="504" font-size="136" textLength="268" lengthAdjust="spacingAndGlyphs">BER</text>
      <text class="t-light" x="7" y="579" font-size="84" textLength="268" lengthAdjust="spacingAndGlyphs">DUNES</text>
    </svg>
  </h1>

  <div class="panel panel--author"></div>
  <div class="bracket bracket--author-v"></div>
  <div class="bracket bracket--author-h"></div>
  <p class="author">ELENA<br>MARCHETTI, MD</p>
</main>
</body>
</html>
```